Awesome law firm seeks great artwork for sign to be installed at local roller skating rink!!

We're a dynamic, law firm that does its work with a difference - we actually care about our clients and our fees are usually lower than most other firms.

We are installing a sign that's 78cm (height) x 158cm (width) to be printed on 3mm Aluminum Composite Panel and installed at a local roller skating rink in Kalamunda, Perth, Western Australia.

Graphics need to be provided in vector .eps (Encapsulated Post Script), .ai (Adobe Illustrator) or PDF format.

We have uploaded a copy of our Logo, which should feature on the sign (we usually have it on the top right of our stationery, but are happy to see other suggestions), together with our practice areas - Family Law, Wills and Estates, Building and Construction, Corporate and Commercial, Local Government, General legal (personal or business).

We don't have a 'slogan' for our firm, but for the roller skating rink sign, we're thinking of something like 'We roll with you", or something similar. Surprise us :)

Sign should also indicate that our team are local to "the Hills", which is how this area (the Kalamunda and surrounding areas of Perth) is known.

Main colors of the sign can include blue, white, black and red (more blue, white and black preferred).

The final design should communicate trust and expertise in law, but have a fun edge (the sign's at a roller skating rink after all and will be seen on every lap as it's in the rink).

The sign must include our website address www.pelbarnlegal.com (note this is still under construction in case you google us :)), our phone number 0491 607 238 and our main email address, which is admin@pelbarnlegal.com

Beyond this, we're happy to see any cool ideas for the design of our sign.

Target Market(s)

Local families and business owners at local roller skating rink

Industry/Entity Type

Legal services

Font styles to use
Serif
Other font styles liked:
• Designer to choose

Colors
0054AA
0677BA
7BADD7
CADEEF
E8F1F8
EB3D1F
EC4F4E
F09395
F8D3D4
FCEDEE

Requirements
Must have
• Logo, contact details, design as per description and can have the words "Get your skates on!"
Nice to have
• Awesome, striking, appealing design - easy to read as you're zooming past on your skates!
Should not have
• Any offensive, explicit, corny or suggestive words and preferably avoid cliché rhyming catch phrases, albeit we do want something fun that has a skating vibe

```html
<!DOCTYPE html>
<html lang="en">
<head>
<meta charset="utf-8">
<title>Pelbarn Legal – Rink Sign</title>
<link rel="stylesheet" href="https://fonts.googleapis.com/css2?family=Source+Serif+4:opsz,wght@8..60,700;8..60,900&family=Tinos:wght@400;700&display=swap">
<style>
  :root {
    --blue: #2a4db8;
    --blue-soft: #3d62c6;
    --red: #e83b20;
    --navy: #14245a;
    --white: #ffffff;
    --photo-light: #eef4f8;
    --photo-mid: #c9d7e2;
    --photo-warm: #8a5a40;
  }
  html, body {
    margin: 0;
    padding: 0;
    width: 1200px;
    height: 592px;
    overflow: hidden;
    background: var(--white);
  }
  .sign {
    position: relative;
    width: 1200px;
    height: 592px;
    overflow: hidden;
  }
  .sign svg { display: block; }
  .headline { font-family: "Source Serif 4", serif; font-weight: 900; fill: var(--blue); }
  .tagline { font-family: "Source Serif 4", serif; font-weight: 700; fill: var(--red); }
  .practice { font-family: "Source Serif 4", serif; font-weight: 700; fill: var(--blue-soft); }
  .brand-name { font-family: "Tinos", serif; font-weight: 400; fill: var(--blue-soft); }
  .contact { font-family: "Tinos", serif; font-weight: 400; fill: var(--white); }
</style>
</head>
<body>
<div class="sign">
  <svg width="1200" height="592" viewBox="0 0 1200 592" xmlns="http://www.w3.org/2000/svg">
    <defs>
      <linearGradient id="photoTone" x1="0" y1="0" x2="1" y2="1">
        <stop offset="0" stop-color="var(--photo-light)"/>
        <stop offset="0.55" stop-color="var(--photo-mid)"/>
        <stop offset="1" stop-color="var(--photo-warm)"/>
      </linearGradient>
    </defs>

    <!-- image area: scales of justice, law books and gavel -->
    <rect class="hero-photo" x="0" y="0" width="700" height="505" fill="url(#photoTone)"
          role="img" aria-label="Photo of scales of justice, open law books and a wooden gavel"/>

    <!-- white message panel -->
    <polygon class="message-panel" points="614,0 1200,0 1200,505 571,505 387,275" fill="var(--white)"/>
    <polygon class="corner-accent" points="1155,0 1200,0 1200,51" fill="var(--navy)"/>
    <polygon class="corner-accent" points="569,505 575,496 581,505" fill="var(--navy)"/>

    <!-- brand name -->
    <text class="brand-name" x="36" y="55" font-size="33" textLength="164" lengthAdjust="spacingAndGlyphs">PELBARN</text>
    <text class="brand-name" x="36" y="119" font-size="56" textLength="146" lengthAdjust="spacingAndGlyphs">LEGAL</text>

    <!-- headline -->
    <text class="headline" x="596" y="140" font-size="124" textLength="522" lengthAdjust="spacingAndGlyphs">WE ROLL</text>
    <text class="headline" x="526" y="268" font-size="140" textLength="659" lengthAdjust="spacingAndGlyphs">WITH YOU</text>

    <!-- tagline -->
    <text class="tagline" x="491" y="334" font-size="60" textLength="683" lengthAdjust="spacingAndGlyphs">Our team are local to the Hills</text>

    <!-- practice areas -->
    <text class="practice" x="557" y="389" font-size="25" textLength="624" lengthAdjust="spacingAndGlyphs">Practice areas - Family Law, Wills and Estates, Building</text>
    <text class="practice" x="572" y="421" font-size="25" textLength="593" lengthAdjust="spacingAndGlyphs">and Construction, Corporate and Commercial, Local</text>
    <text class="practice" x="598" y="454" font-size="25" textLength="542" lengthAdjust="spacingAndGlyphs">Government, General legal (personal or business</text>

    <!-- contact band -->
    <rect class="contact-band" x="0" y="505" width="1200" height="87" fill="var(--red)"/>

    <g class="icon-globe" fill="none" stroke="var(--white)" stroke-width="2">
      <circle cx="28" cy="551" r="14"/>
      <ellipse cx="28" cy="551" rx="6" ry="14"/>
      <line x1="14" y1="551" x2="42" y2="551"/>
      <path d="M16 544 H40 M16 558 H40"/>
    </g>
    <text class="contact" x="55" y="563" font-size="38" textLength="335" lengthAdjust="spacingAndGlyphs">www.pelbarnlegal.com</text>

    <g class="icon-mail" fill="none" stroke="var(--white)" stroke-width="2.5">
      <rect x="426" y="542" width="31" height="21"/>
      <path d="M426 542 L441.5 555 L457 542 M426 563 L437 552 M457 563 L446 552"/>
    </g>
    <text class="contact" x="473" y="563" font-size="38" textLength="378" lengthAdjust="spacingAndGlyphs">admin@pelbarnlegal.com</text>

    <g class="icon-phone">
      <path d="M888 540 C886 548 893 562 906 568 C909 569 912 567 913 565 L915 561 L908 556 L904 559 C899 556 895 551 893 546 L897 543 L892 537 L889 538 Z" fill="var(--white)"/>
      <path d="M903 540 A10 10 0 0 1 911 548 M903 533 A17 17 0 0 1 918 548" fill="none" stroke="var(--white)" stroke-width="2.2"/>
    </g>
    <text class="contact" x="934" y="563" font-size="38" textLength="241" lengthAdjust="spacingAndGlyphs">0491 607 238</text>
  </svg>
</div>
</body>
</html>
```